Client questionnaire

Quillon Ravenmoor Group (www.quillonravenmoor.com.au) needs a document designed to bring out as a questionnaire to speak with potential clients. Sales staff and planners will use this in introductions to ask basic questions but to also scribble notes and draw pictures on top of the graph.
I've attached two files which are the content that we wish to include.
1. Financial life cycle: this has two pages. Please design it so that the financial snap shot is on a different page than the lifecycle and graph. I will leave it to the designer to decide whether landscape or portrait is best - please ensure though that they are both landscape or both portrait on this document as they will be printed back to back on the same sheet.
2. Goals diagram - please theme this in the same way as the above document.
3. I've attached the logo to be used too - filename: QuillonRavenmoorgroup.eps

Group

```html
<!DOCTYPE html>
<html lang="en">
<head>
<meta charset="utf-8">
<title>Your financial snapshot – Quillon Ravenmoor Group</title>
<link rel="stylesheet" href="https://fonts.googleapis.com/css2?family=Source+Sans+3:wght@400;600&family=Cormorant+SC:wght@500&display=swap">
<style>
  :root {
    --brand-blue: #0b69a3;
    --rule: #b9bcc4;
    --shade: #a7abb3;
    --ink: #2e2e2e;
    --mark: #3d3d3d;
    --panel: #f3f3f3;
    --paper: #ffffff;
  }
  * { box-sizing: border-box; margin: 0; padding: 0; }
  html, body { width: 1200px; height: 849px; overflow: hidden; background: var(--paper); }
  body { font-family: "Source Sans 3", Arial, sans-serif; color: var(--ink); }
  .sheet { position: relative; width: 1200px; height: 849px; }

  .brand-block {
    position: absolute; left: 15px; top: 10px; width: 210px; height: 180px;
    background: var(--panel);
    display: flex; flex-direction: column; align-items: center; justify-content: center; gap: 14px;
  }
  .brand-dot { width: 70px; height: 70px; border-radius: 50%; border: 4px solid var(--mark); }
  .brand-name {
    font-size: 22px; font-weight: 600; color: var(--mark);
    text-align: center; line-height: 1.15; width: 180px;
  }

  .edge-motif {
    position: absolute; left: 0; top: 205px; width: 150px; height: 644px;
    background: linear-gradient(90deg, #e4e4e4 0%, #f6f6f6 60%, rgba(255,255,255,0) 100%);
  }

  .page-title {
    position: absolute; right: 22px; top: 24px;
    font-family: "Cormorant SC", "Times New Roman", serif;
    font-weight: 500; font-size: 30px; letter-spacing: 0.5px; color: #222;
  }

  .form-frame {
    position: absolute; left: 252px; top: 81px; width: 930px; height: 595px;
    border: 1px solid var(--rule);
  }
  table { width: 100%; border-collapse: collapse; table-layout: fixed; font-size: 14.5px; }
  td, th { border: 1px solid var(--rule); padding: 0 6px; height: 24px; text-align: left; font-weight: 400; white-space: nowrap; }
  tr > :first-child { border-left: none; }
  tr > :last-child { border-right: none; }
  .band th {
    background: var(--brand-blue); color: #fff; font-weight: 600; font-size: 15px;
    border-color: var(--brand-blue); padding-left: 8px;
  }
  .heads th { text-align: center; }
  .heads th:first-child, .heads th:last-child { text-align: left; }
  .heads th:last-child { padding-left: 19px; }
  .spacer td { height: 29px; }
  .spacer-sm td { height: 19px; }
  .spacer-xs td { height: 12px; }
  .shaded { background: var(--shade); }
  .amount { padding-left: 8px; }
  .liab-heads th { height: 29px; }
  .details-table td { border-top: none; }
  .details-table tr:first-child td { border-top: 1px solid var(--rule); }

  .consent {
    position: absolute; left: 163px; top: 705px; width: 1020px;
    font-size: 9.4px; line-height: 1.22; color: #222;
  }
  .sign-off {
    position: absolute; left: 565px; top: 795px; font-size: 14px; line-height: 17px; color: #222;
  }
  .sign-line { display: inline-block; width: 505px; border-bottom: 1px solid #333; margin-left: 3px; }
  .date-slot { display: inline-block; width: 24px; border-bottom: 1px solid #333; }
</style>
</head>
<body>
<div class="sheet">
  <div class="brand-block">
    <div class="brand-dot"></div>
    <div class="brand-name">Quillon Ravenmoor Group</div>
  </div>
  <div class="edge-motif" role="img" aria-label="Decorative ring motif along the left edge"></div>

  <h1 class="page-title">Your financial snapshot…</h1>

  <div class="form-frame">
    <table class="details-table">
      <colgroup><col style="width:465px"><col></colgroup>
      <tr class="band"><th>Your details</th><th style="padding-left:15px">Partner’s details</th></tr>
      <tr><td>Name:</td><td style="padding-left:16px">Name:</td></tr>
      <tr><td>D.O.B:</td><td style="padding-left:16px">D.O.B:</td></tr>
      <tr><td>Occupation:</td><td style="padding-left:16px">Occupation:</td></tr>
      <tr><td>Annual salary:&nbsp; $</td><td style="padding-left:16px">Annual salary:&nbsp; $</td></tr>
      <tr><td>Children:</td><td style="padding-left:16px">Children:</td></tr>
      <tr class="spacer"><td colspan="2" style="border-bottom:none"></td></tr>
    </table>

    <table>
      <colgroup><col style="width:236px"><col style="width:156px"><col style="width:129px"><col></colgroup>
      <tr class="band"><th colspan="4">Assets</th></tr>
      <tr class="heads"><th>Description</th><th>Date purchased</th><th>Value</th><th>Details</th></tr>
      <tr><td>Residential home</td><td></td><td class="amount">$</td><td></td></tr>
      <tr><td>Investment property</td><td></td><td class="amount">$</td><td></td></tr>
      <tr><td>Cash</td><td></td><td class="amount">$</td><td></td></tr>
      <tr><td>Car(s)</td><td></td><td class="amount">$</td><td></td></tr>
      <tr><td>Superannuation</td><td></td><td class="amount">$</td><td></td></tr>
      <tr><td>Total Assets</td><td class="shaded"></td><td class="amount">$</td><td></td></tr>
      <tr class="spacer-sm"><td></td><td></td><td></td><td></td></tr>
    </table>

    <table>
      <colgroup><col style="width:236px"><col style="width:99px"><col style="width:79px"><col style="width:107px"><col></colgroup>
      <tr class="band"><th colspan="5">Liabilities</th></tr>
      <tr class="heads liab-heads"><th>Description</th><th>Lender</th><th>Term</th><th>Amount</th><th>Details</th></tr>
      <tr><td>Residential home</td><td></td><td></td><td class="amount">$</td><td></td></tr>
      <tr><td>Investment property</td><td></td><td></td><td class="amount">$</td><td></td></tr>
      <tr><td>Personal loan</td><td></td><td></td><td class="amount">$</td><td></td></tr>
      <tr><td>Car loan</td><td></td><td></td><td class="amount">$</td><td></td></tr>
      <tr><td>Credit cards</td><td></td><td></td><td class="amount">$</td><td></td></tr>
      <tr><td>Total Liabilities</td><td class="shaded" colspan="2"></td><td class="amount">$</td><td></td></tr>
      <tr class="spacer-xs"><td style="border-bottom:none"></td><td style="border-bottom:none"></td><td style="border-bottom:none"></td><td style="border-bottom:none"></td><td style="border-bottom:none"></td></tr>
    </table>
  </div>

  <p class="consent">I/We consent to you using personal and credit information about me/us for the purpose of arranging or providing credit, insuring credit, and for direct marketing of products and services offered by you or any organisation you are affiliated with or represent. The personal information provided by me/us will be held by you. I/We can gain access to the information by contacting you. I/We have the right to request not to receive marketing material. You may disclose personal information about me/us as required by law, or to organisations involved in providing credit to me/us, any of your associates or contractors, (including, for example, stationary printing houses, mail houses, lawyers, accountants), or people considering acquiring or taking an interest in your business or assets. I/We hereby authorise you to receive information from any lender about our credit affairs, and to provide any relevant real estate agent, lawyer, or conveyance with details of whether finance has been approved for us, and if it has the terms of that approval, including providing a copy of any approval letter. I/we may disclose personal information to any industry body, tribunal, court or otherwise in connection with any complain regarding the approval or management of your loan - for example if a complaint is lodged about me/us or the lender.</p>

  <div class="sign-off">
    <div>Signature(s):<span class="sign-line"></span></div>
    <div>Date: <span class="date-slot"></span> /<span class="date-slot"></span> /<span class="date-slot"></span></div>
  </div>
</div>
</body>
</html>
```